Stationary Design for Stunning new Logo

I need to envelopes, letterhead, business cards designed to compliment our new logo.

We are a 25 year old printing company going through a brand refresh. All items should have the design extended to both sides for full print ability.

Industry/Entity Type

Printing

Requirements
Must have
• It must utilize the new logo & colors PMS 300 & PMS 295.

```html
<!DOCTYPE html>
<html lang="en">
<head>
<meta charset="utf-8">
<title>Tagwell Stationery</title>
<link href="https://fonts.googleapis.com/css2?family=PT+Sans+Narrow:wght@400;700&family=Questrial&display=swap" rel="stylesheet">
<style>
  :root {
    --pms-300: #1565d8;
    --pms-295: #0b3a8f;
    --bright: #3f93ff;
    --ink: #1d2230;
    --grey-text: #555b66;
    --paper: #ffffff;
    --stage: #c9ccd0;
  }
  * { box-sizing: border-box; margin: 0; padding: 0; }
  html, body { width: 1200px; height: 848px; overflow: hidden; }
  body { background: var(--stage); position: relative; font-family: "PT Sans Narrow", "Arial Narrow", sans-serif; color: var(--ink); }

  .sheet { position: absolute; background: var(--paper); overflow: hidden; box-shadow: 2px 3px 6px rgba(0,0,0,0.35); }

  .band { position: absolute; left: 0; right: 0; height: 6px;
    background: linear-gradient(90deg, var(--pms-295) 0%, var(--pms-300) 45%, var(--bright) 70%, var(--pms-300) 100%); }
  .band.top { top: 0; }
  .band.bottom { bottom: 0; }

  .brand { position: absolute; display: flex; align-items: center; gap: 4px; color: var(--pms-300); font-weight: 700; letter-spacing: 0.5px; line-height: 1; white-space: nowrap; }
  .brand .dot { border-radius: 50%; background: var(--pms-300); }

  .label { color: var(--pms-300); font-weight: 700; }

  /* letterhead */
  .letterhead { left: 30px; top: 37px; width: 542px; height: 765px; }
  .letterhead .brand { right: 28px; top: 16px; font-size: 24px; }
  .letterhead .brand .dot { width: 17px; height: 17px; }
  .lh-footer { position: absolute; left: 25px; right: 25px; bottom: 22px; display: flex; font-family: "Questrial", sans-serif; font-size: 10px; line-height: 1.07; color: var(--grey-text); white-space: nowrap; }
  .lh-footer .label { font-family: "PT Sans Narrow", sans-serif; font-size: 10px; }
  .lh-footer .col-a { width: 174px; }
  .lh-footer .col-b { width: 181px; }
  .lh-footer .col-c { width: 100px; }
  .lh-footer .web { color: var(--pms-300); font-family: "PT Sans Narrow", sans-serif; font-weight: 700; font-size: 11px; margin-top: 8px; }
  .lh-footer .mark { width: 34px; height: 34px; border-radius: 50%; background: var(--pms-300); margin-top: 4px; }

  /* cards */
  .card { width: 255px; height: 153px; white-space: nowrap; }
  .card .brand { font-size: 17px; }
  .card .brand .dot { width: 12px; height: 12px; }
  .card-a { left: 623px; top: 37px; }
  .card-b { left: 893px; top: 37px; }
  .card-c { left: 623px; top: 215px; }
  .card-d { left: 891px; top: 215px; }
  .card-a .brand { right: 35px; top: 16px; }
  .card-b .brand { left: 20px; top: 16px; }
  .card-c .brand, .card-d .brand { left: 50%; transform: translateX(-50%); top: 30px; }
  .holder { position: absolute; right: 63px; top: 50px; text-align: right; font-family: "Questrial", sans-serif; }
  .holder .name { font-size: 19px; color: var(--ink); }
  .holder .role { font-size: 11px; font-style: italic; margin-right: 16px; }
  .card-a .contact { position: absolute; right: 25px; top: 111px; text-align: right; font-size: 10px; line-height: 1.45; }
  .card-b .contact { position: absolute; left: 27px; top: 67px; font-size: 9px; line-height: 1.3; }
  .card-c .contact { position: absolute; left: 8px; top: 104px; font-size: 9.5px; line-height: 1.3; }
  .card-d .contact { position: absolute; left: 14px; top: 104px; font-size: 9.5px; line-height: 1.3; }
  .card .web { position: absolute; color: var(--pms-300); font-weight: 700; font-size: 11px; }
  .card-b .web { right: 42px; top: 121px; }
  .card-d .web-inline { color: var(--pms-300); font-weight: 700; font-size: 11px; }
  .card .mark { position: absolute; width: 20px; height: 20px; border-radius: 50%; background: var(--pms-300); }
  .card-b .mark { right: 17px; top: 116px; }
  .card-d .mark { right: 12px; top: 120px; }
  .card .band { height: 7px; }

  /* envelopes */
  .env-back { left: 595px; top: 403px; width: 545px; height: 275px; }
  .env-back .flap { position: absolute; left: 0; top: 0; }
  .env-back .web { position: absolute; left: 0; width: 545px; top: 61px; text-align: center; color: #fff; font-weight: 700; font-size: 10px; }
  .env-front { left: 640px; top: 540px; width: 542px; height: 270px; }
  .env-front .brand { left: 20px; top: 20px; font-size: 17px; }
  .env-front .brand .dot { width: 12px; height: 12px; }
  .env-front .return { position: absolute; left: 36px; top: 52px; font-size: 11.5px; font-weight: 700; line-height: 1.15; }
</style>
</head>
<body>

<section class="sheet letterhead" aria-label="Letterhead">
  <div class="band top"></div>
  <div class="brand"><span class="dot"></span>TAGWELL</div>
  <footer class="lh-footer">
    <div class="col-a">
      <div><span class="label">OFFICE</span> Tagwell, Inc. 2715</div>
      <div>Birchmont Commerce Way</div>
      <div>Alder Falls, GA 30519</div>
      <div><span class="label">POSTAL ADDRESS</span> Tagwell, Inc.</div>
      <div>POB 412 Alder Falls, GA 30520</div>
    </div>
    <div class="col-b">
      <div><span class="label">Sales</span> sales@tagwell.co</div>
      <div><span class="label">Customer Service</span> service@tagwell.co</div>
      <div><span class="label">Orders</span> orders@tagwell.co</div>
      <div><span class="label">Art</span> art@tagwell.co</div>
      <div><span class="label">Shipping</span> shipping@tagwell.co</div>
    </div>
    <div class="col-c">
      <div><span class="label">Free T</span> 800.555.0142</div>
      <div><span class="label">Local T</span> 770.555.0187</div>
      <div><span class="label">Fax</span> 770.555.0189</div>
      <div class="web">www.tagwell-print.com</div>
    </div>
    <div class="mark"></div>
  </footer>
  <div class="band bottom"></div>
</section>

<section class="sheet card card-a" aria-label="Business card front">
  <div class="brand"><span class="dot"></span>TAGWELL</div>
  <div class="holder"><div class="name">Project Owner</div><div class="role">director</div></div>
  <div class="contact">
    <div><span class="label">M</span> 800.555.0100 &nbsp;<span class="label">E</span> name@tagwell.co</div>
    <div><span class="label">Free T</span> 800.555.0142 &nbsp;<span class="label">Local T</span> 770.555.0187 &nbsp;<span class="label">Fax</span> 770.555.0189</div>
  </div>
  <div class="band bottom"></div>
</section>

<section class="sheet card card-b" aria-label="Business card back">
  <div class="brand"><span class="dot"></span>TAGWELL</div>
  <div class="contact">
    <div><span class="label">OFFICE</span> Tagwell, Inc. 2715</div>
    <div>Birchmont Commerce Way</div>
    <div>Alder Falls, GA 30519</div>
    <div><span class="label">POSTAL ADDRESS</span> Tagwell, Inc.</div>
    <div>POB 412 Alder Falls, GA 30520</div>
  </div>
  <div class="web">www.tagwell-print.com</div>
  <span class="mark"></span>
  <div class="band bottom"></div>
</section>

<section class="sheet card card-c" aria-label="Business card, office details">
  <div class="band top"></div>
  <div class="brand"><span class="dot"></span>TAGWELL</div>
  <div class="contact">
    <div><span class="label">OFFICE</span> Tagwell, Inc. 2715 Birchmont Commerce Way, Alder Falls, GA 30519</div>
    <div><span class="label">POSTAL ADDRESS</span> Tagwell, Inc. POB 412 Alder Falls, GA 30520</div>
    <div><span class="label">Free T</span> 800.555.0142 &nbsp;<span class="label">Local T</span> 770.555.0187 &nbsp;<span class="label">Fax</span> 770.555.0189</div>
  </div>
  <div class="band bottom"></div>
</section>

<section class="sheet card card-d" aria-label="Business card, department contacts">
  <div class="band top"></div>
  <div class="brand"><span class="dot"></span>TAGWELL</div>
  <div class="contact">
    <div><span class="label">Sales</span> sales@tagwell.co &nbsp;<span class="label">Customer Service</span> service@tagwell.co</div>
    <div><span class="label">Orders</span> orders@tagwell.co &nbsp;<span class="label">Art</span> art@tagwell.co</div>
    <div><span class="label">Shipping</span> shipping@tagwell.co &nbsp;&nbsp;&nbsp;&nbsp;<span class="web-inline">www.tagwell-print.com</span></div>
  </div>
  <span class="mark"></span>
  <div class="band bottom"></div>
</section>

<section class="sheet env-back" aria-label="Envelope back">
  <svg class="flap" width="545" height="130" viewBox="0 0 545 130" aria-hidden="true">
    <defs>
      <linearGradient id="flapFill" x1="0" y1="0" x2="0" y2="1">
        <stop offset="0" stop-color="#0b3a8f"/>
        <stop offset="1" stop-color="#1452b8"/>
      </linearGradient>
    </defs>
    <polygon points="0,0 545,0 275,125" fill="url(#flapFill)"/>
  </svg>
  <div class="web">www.tagwell-print.com</div>
</section>

<section class="sheet env-front" aria-label="Envelope front">
  <div class="brand"><span class="dot"></span>TAGWELL</div>
  <div class="return">
    <div>Tagwell, Inc. 2715</div>
    <div>Birchmont Commerce Way</div>
    <div>Alder Falls, GA 30519</div>
  </div>
</section>

</body>
</html>
```